New business card/stationary for a consulting company

I am looking for a clean and very professional looking business card for my consulting company as well as corresponding stationary. I am uploading our logo. I like simple and powerful for the feel. No graphics but I am open on everything else. Below is my contact information but would like the final to be in a version I can add my employees information into and print. Thank you.

Daniel Whitcombe
dan@fernlowadvisory.com
2837 North 9th Avenue, Summit Floor, Elm Crest, Vermont 60483
www.fernlowadvisory.com

Industry/Entity Type

Consulting

Contact Information for Business Card

Daniel Whitcombe
dan@fernlowadvisory.com
www.fernlowadvisory.com

Font styles to use
Serif
Sans Serif

Requirements
Must have
• Our logo and the business card details.
Nice to have
• our website www.fernlowadvisory.com

```html
<!DOCTYPE html>
<html lang="en">
<head>
<meta charset="utf-8">
<title>Fernlow Advisory – Business Card</title>
<link rel="stylesheet" href="https://fonts.googleapis.com/css2?family=Questrial&family=Source+Sans+3:wght@400&display=swap">
<style>
  :root {
    --stage: #555555;
    --paper: #ffffff;
    --navy: #0b0b6e;
    --navy-deep: #08086a;
    --ink: #222222;
  }
  html, body {
    margin: 0;
    padding: 0;
    width: 1200px;
    height: 900px;
    overflow: hidden;
    background: var(--stage);
  }
  .stage {
    position: relative;
    width: 1200px;
    height: 900px;
  }
  .card {
    position: absolute;
    top: 306px;
    width: 439px;
    height: 271px;
  }
  .card-front {
    left: 149px;
    background: var(--paper);
    color: var(--navy);
  }
  .card-back {
    left: 608px;
    background: var(--navy-deep);
  }
  .brand-mark {
    position: absolute;
    left: 248px;
    top: 38px;
    width: 44px;
    height: 44px;
    background: var(--navy);
  }
  .brand-name {
    position: absolute;
    right: 30px;
    top: 94px;
    margin: 0;
    font-family: "Questrial", sans-serif;
    font-weight: 400;
    font-size: 22px;
    letter-spacing: 0.3px;
    white-space: nowrap;
  }
  .holder {
    position: absolute;
    left: 27px;
    top: 152px;
    width: 382px;
    display: flex;
    align-items: center;
    gap: 10px;
  }
  .holder-name {
    margin: 0;
    font-family: "Questrial", sans-serif;
    font-weight: 400;
    font-size: 14px;
    letter-spacing: 0.4px;
    white-space: nowrap;
  }
  .holder-rule {
    flex: 1;
    height: 1px;
    background: var(--navy);
  }
  .address {
    position: absolute;
    left: 27px;
    top: 197px;
    margin: 0;
    font-family: "Source Sans 3", sans-serif;
    font-style: normal;
    font-size: 12.5px;
    line-height: 16px;
    color: var(--ink);
  }
  .contact {
    position: absolute;
    right: 30px;
    top: 213px;
    margin: 0;
    padding: 0;
    list-style: none;
    font-family: "Source Sans 3", sans-serif;
    font-size: 12.5px;
    line-height: 16px;
    color: var(--ink);
    text-align: right;
  }
  .contact li {
    display: flex;
    justify-content: flex-end;
    align-items: center;
    gap: 3px;
  }
  .contact-icon {
    width: 10px;
    height: 10px;
    fill: var(--navy);
  }
  .back-field {
    position: absolute;
    inset: 0;
    background: var(--navy-deep);
  }
</style>
</head>
<body>
  <main class="stage">
    <section class="card card-front" aria-label="Business card front">
      <div class="brand-mark" aria-hidden="true"></div>
      <h1 class="brand-name">FERNLOW ADVISORY</h1>

      <div class="holder">
        <h2 class="holder-name">DANIEL WHITCOMBE</h2>
        <span class="holder-rule"></span>
      </div>

      <address class="address">
        2837 North 9th Avenue,<br>
        Summit Floor, Elm Crest,<br>
        Vermont 60483
      </address>

      <ul class="contact">
        <li>dan@fernlowadvisory.com
          <svg class="contact-icon" viewBox="0 0 10 10" aria-hidden="true">
            <rect x="0" y="2" width="10" height="7"/>
            <path d="M0.5 2.6 L5 6 L9.5 2.6" fill="none" stroke="#fff" stroke-width="0.9"/>
          </svg>
        </li>
        <li>www.fernlowadvisory.com
          <svg class="contact-icon" viewBox="0 0 10 10" aria-hidden="true">
            <circle cx="5" cy="5" r="5"/>
            <path d="M3 2.5 Q5 3.5 4 5 Q3 6 5 7.5 M6.5 2 Q7.5 4 6.5 5" fill="none" stroke="#fff" stroke-width="0.8"/>
          </svg>
        </li>
      </ul>
    </section>

    <section class="card card-back" aria-label="Business card back">
      <div class="back-field" role="img" aria-label="Navy background with a repeating grid of the company brand tiles, one tile highlighted in white"></div>
    </section>
  </main>
</body>
</html>
```